Business Card Ayurvedic Massage

I'm starting with my ayurvedic massage business and need a business card design. The design should be inline with my brand/logo as well as with the design of my website (www.lumo-thara.ch).
Front: logo and text "Ayurvedische Massagen"
back: name and adress (see details https://www.lumo-thara.ch/kontakt.html)

```html
<!DOCTYPE html>
<html lang="de">
<head>
<meta charset="utf-8">
<title>lumo-thara – Visitenkarte</title>
<link rel="stylesheet" href="https://fonts.googleapis.com/css2?family=Tinos:wght@400;700&display=swap">
<style>
  :root {
    --backdrop: #2a2a2a;
    --card-red: #c4141f;
    --card-red-deep: #8e0b13;
    --card-red-light: #d8232c;
    --card-white: #ffffff;
    --gold: #d9a531;
    --gold-brown: #b9771f;
    --name-red: #b0151c;
    --shadow: rgba(0, 0, 0, 0.55);
  }
  * { box-sizing: border-box; margin: 0; padding: 0; }
  html, body {
    width: 1200px;
    height: 900px;
    overflow: hidden;
    background: var(--backdrop);
    font-family: "Tinos", "Times New Roman", serif;
  }
  .stage {
    width: 1200px;
    height: 900px;
    display: flex;
    flex-direction: column;
    align-items: center;
    justify-content: center;
    gap: 44px;
  }
  .card {
    position: relative;
    width: 620px;
    height: 354px;
    border-radius: 26px;
    overflow: hidden;
    box-shadow: 0 14px 30px var(--shadow);
  }
  .card-front {
    background: var(--card-red);
  }
  .front-pattern {
    position: absolute;
    inset: 0;
    background: radial-gradient(ellipse at 55% 45%, var(--card-red-light) 0%, var(--card-red) 45%, var(--card-red-deep) 100%);
  }
  .front-brand {
    position: absolute;
    inset: 0;
    display: flex;
    flex-direction: column;
    align-items: center;
    justify-content: center;
    gap: 16px;
  }
  .brand-name {
    display: flex;
    align-items: center;
    gap: 14px;
    font-weight: 700;
    color: var(--gold);
  }
  .brand-dot {
    width: 16px;
    height: 16px;
    border-radius: 50%;
    background: var(--gold);
  }
  .card-front .brand-name { font-size: 48px; }
  .tagline {
    font-size: 19px;
    letter-spacing: 0.06em;
    color: var(--gold);
    text-transform: uppercase;
  }
  .card-back {
    background: var(--card-white);
    display: flex;
    flex-direction: column;
    align-items: center;
    justify-content: center;
    gap: 18px;
  }
  .card-back .brand-name {
    font-size: 38px;
    color: var(--gold-brown);
  }
  .card-back .brand-dot { background: var(--gold-brown); }
  .contact {
    font-style: normal;
    text-align: center;
    color: var(--gold-brown);
    font-size: 18px;
    line-height: 1.28;
  }
  .contact-name {
    color: var(--name-red);
    font-weight: 700;
    font-size: 18px;
    text-transform: uppercase;
  }
</style>
</head>
<body>
<main class="stage">
  <section class="card card-front" aria-label="Vorderseite">
    <div class="front-pattern" role="img" aria-label="Rotes Blumenmuster mit angedeuteter Palastsilhouette"></div>
    <div class="front-brand">
      <div class="brand-name"><span class="brand-dot"></span>lumo-thara</div>
      <p class="tagline">Ayurvedische Massagen</p>
    </div>
  </section>

  <section class="card card-back" aria-label="Rückseite">
    <div class="brand-name"><span class="brand-dot"></span>lumo-thara</div>
    <address class="contact">
      <p class="contact-name">Mira Tanner</p>
      <p>lumo-thara, Lindenweg 14, 8752 Näfels (GL)</p>
      <p>Phone: +41 77 380 26 14</p>
      <p>E mail: info@lumo-thara.ch</p>
      <p>www.lumo-thara.ch</p>
    </address>
  </section>
</main>
</body>
</html>
```